Flyer Design

i would like a double sided two different treatments colour scheme is red and white first side….
brightline grins (teeth whitening )

we use a non peroxide gel so no sensitivity at all and completely pain free cosmetic procedure.
we offer two different treatments…
20 minute express £30 each or 2 people for £50
45 minute premium (longer lasting) £50 each or 2 people for £80
i also do gift certificates perfect for birthdays christmas or just the one you love
i would like a voucher added on here if they bring the voucher they can claim a free top up pen or have an extra 10% off
i would like my details on here
name rebecca dowd
number 01632960418
address 27 heol y felin pentwyn cf145qt
email dowdkevindowd@mailbox-example.co.uk

other side…. again colours in red and white
velvetwave laser lipo
A non-invasive treatment that every salon and spa must have! Say no to Liposuction, surgery or crash diet. This new innovative laser technology will break down the fat cells and promote the triglyceride in the cells overflow. The fat cells are significantly reduced, achieving weight loss immediately. At the same time, the outflow of the glycerol and free acids are decomposed in part by capillaries and lymphatic microtubule, partly transformed into energy by movement, and partly excreted by the kidneys. The velvetwave laser lipo can reduce from 2-15cm of body fat after a single treatment. The procedure is fast, relaxing and effective on any body parts without causing any side effects to the client.

cost is £40 per session or full course of 8 sessions at £199
i also do gift certificates perfect for birthdays, christmas or just the one you love.
also a voucher with an extra 10% off

name: rebecca dowd
number: 01632 960418
address: 27 heol y felin pentwyn cf145qt
email address: dowdkevindowd@mailbox-example.co.uk

Weight

```html
<!DOCTYPE html>
<html lang="en">
<head>
<meta charset="utf-8">
<title>Brightline Grins &amp; Velvetwave Laser Lipo – Flyer</title>
<link rel="stylesheet" href="https://fonts.googleapis.com/css2?family=Comfortaa:wght@400;700&family=Playfair+Display:ital,wght@1,700&display=swap">
<style>
  :root {
    --red: #d71f2a;
    --red-deep: #c21822;
    --white: #ffffff;
    --paper: #f7f6f4;
    --ink: #1a1a1a;
    --grey-text: #9a9a9a;
    --stage: #d9d9d9;
    --skin-light: #efe4dc;
    --skin-mid: #d9c2b4;
    --teeth-yellow: #e8d9a8;
    --gum: #c8545a;
    --teeth-white: #f4f6f8;
    --lips: #c9454d;
  }
  * { box-sizing: border-box; margin: 0; padding: 0; }
  html, body { width: 1200px; height: 720px; overflow: hidden; }
  body {
    background: var(--stage);
    font-family: "Comfortaa", "Century Gothic", sans-serif;
    color: var(--ink);
    display: flex;
    justify-content: center;
    align-items: center;
    gap: 44px;
  }
  .flyer {
    position: relative;
    width: 467px;
    height: 660px;
    background: var(--paper);
  }
  .flyer::before {
    content: "";
    position: absolute;
    inset: 10px;
    border: 2px solid var(--red);
    pointer-events: none;
  }
  .block { position: absolute; }
  .photo { position: absolute; border-radius: 2px; }

  /* Teeth whitening side */
  .brand-title {
    left: 24px; top: 18px;
    font-family: "Playfair Display", Georgia, serif;
    font-style: italic; font-weight: 700;
    font-size: 30px; color: var(--red);
  }
  .tagline {
    left: 26px; top: 60px; width: 190px;
    font-size: 13px; line-height: 1.25; color: var(--grey-text);
  }
  .photo-portrait {
    right: 22px; top: 16px; width: 200px; height: 100px;
    background: linear-gradient(90deg, var(--paper) 0%, var(--skin-light) 45%, var(--skin-mid) 100%);
  }
  .info-panel {
    left: 22px; top: 124px; width: 230px; height: 214px;
    background: var(--red);
    color: var(--white);
    font-size: 12px; line-height: 1.35;
    text-align: center;
    padding: 12px 12px;
    display: flex; flex-direction: column; gap: 9px;
  }
  .photo-teeth-before {
    left: 262px; top: 128px; width: 182px; height: 100px;
    background: linear-gradient(180deg, var(--gum) 0%, var(--teeth-yellow) 30%, var(--teeth-yellow) 70%, var(--gum) 100%);
  }
  .photo-teeth-after {
    left: 262px; top: 236px; width: 182px; height: 100px;
    background: linear-gradient(180deg, var(--gum) 0%, var(--teeth-white) 30%, var(--teeth-white) 70%, var(--gum) 100%);
  }
  .after-label {
    position: absolute; right: 10px; top: 8px;
    font-size: 12px; font-weight: 700; color: var(--white);
    text-shadow: 0 0 3px rgba(0,0,0,.5);
  }
  .photo-lips {
    left: 22px; top: 350px; width: 160px; height: 130px;
    background: linear-gradient(90deg, var(--skin-mid) 0%, var(--lips) 35%, var(--teeth-white) 55%, var(--lips) 75%, var(--skin-mid) 100%);
  }
  .gift-note {
    left: 196px; top: 372px; width: 250px;
    font-size: 15px; line-height: 1.3; color: var(--red);
    text-align: center;
  }
  .voucher {
    border: 2px dashed var(--red);
    display: flex; flex-direction: column; justify-content: center; align-items: center;
    text-align: center;
  }
  .voucher-smile {
    left: 22px; top: 500px; width: 206px; height: 138px;
    font-size: 13px; line-height: 1.35; font-weight: 700;
  }
  .accent { color: var(--red); }
  .contact-card {
    background: var(--red);
    color: var(--white);
    text-align: center;
    font-size: 12.5px; line-height: 1.45;
    display: flex; flex-direction: column; justify-content: center;
    padding: 8px 6px;
  }
  .contact-email { font-size: 10px; overflow-wrap: anywhere; }
  .contact-smile { left: 240px; top: 506px; width: 206px; height: 118px; }

  /* Laser lipo side */
  .photo-body-strip {
    left: 22px; top: 22px; width: 272px; height: 150px;
    background: linear-gradient(90deg, var(--skin-light) 0%, var(--white) 40%, var(--skin-mid) 100%);
  }
  .brand-mark {
    left: 304px; top: 70px; width: 142px;
    display: flex; align-items: center; gap: 6px;
    font-size: 12px; font-weight: 700; color: var(--red); line-height: 1.2;
  }
  .brand-mark .dot {
    flex: none; width: 14px; height: 14px; border-radius: 50%; background: var(--red);
  }
  .lipo-panel {
    left: 22px; top: 186px; width: 424px; height: 216px;
    background: var(--red);
    color: var(--white);
    text-align: center;
    padding: 10px 14px;
  }
  .lipo-heading { font-size: 13px; font-weight: 700; margin-bottom: 5px; }
  .lipo-copy { font-size: 9.4px; line-height: 1.38; }
  .photo-waist {
    left: 22px; top: 414px; width: 220px; height: 110px;
    background: linear-gradient(90deg, var(--skin-mid) 0%, var(--skin-light) 50%, var(--skin-mid) 100%);
  }
  .price-note {
    left: 254px; top: 414px; width: 192px;
    text-align: center; font-size: 12px; line-height: 1.35;
    display: flex; flex-direction: column; gap: 8px;
  }
  .price-note .gift { color: var(--red); }
  .contact-lipo { left: 22px; top: 534px; width: 220px; height: 106px; }
  .voucher-lipo {
    left: 254px; top: 540px; width: 192px; height: 98px;
    font-size: 17px; font-weight: 700; line-height: 1.3;
  }
</style>
</head>
<body>

  <section class="flyer flyer-lipo" aria-label="Velvetwave Laser Lipo flyer">
    <div class="photo photo-body-strip" role="img" aria-label="Photographs of a slim waist and body in white underwear"></div>
    <div class="block brand-mark"><span class="dot"></span><span>Velvetwave Laser Lipo</span></div>

    <div class="block lipo-panel">
      <p class="lipo-heading">Velvetwave Laser Lipo</p>
      <p class="lipo-copy">A non-invasive treatment that every salon and spa must have! Say no to Liposuction, surgery or crash diet. This new innovative laser technology will break down the fat cells and promote the triglyceride in the cells overflow. The fat cells are significantly reduced, achieving weight loss immediately. At the same time, the outflow of the glycerol and free acids are decomposed in part by capillaries and lymphatic microtubule, partly transformed into energy by movement, and partly excreted by the kidneys. The Velvetwave laser lipo can reduce from 2-15cm of body fat after a single treatment. The procedure is fast, relaxing and effective on any body parts without causing any side effects to the client.</p>
    </div>

    <div class="photo photo-waist" role="img" aria-label="Photograph of a waist being measured with a tape measure"></div>
    <div class="block price-note">
      <p>£40 per session or full course of 8 sessions at £199</p>
      <p class="gift">I also do gift certificates perfect for birthdays, christmas or just the one you love</p>
    </div>

    <address class="block contact-card contact-lipo">
      <span>Rebecca Dowd</span>
      <span>01632 960418</span>
      <span>27 Heol y Felin Pentwyn CF145QT</span>
      <span class="contact-email">dowdkevindowd@mailbox-example.co.uk</span>
    </address>

    <div class="block voucher voucher-lipo">
      <p>extra 10% off<br>with this Voucher</p>
    </div>
  </section>

  <section class="flyer flyer-smile" aria-label="Brightline Grins teeth whitening flyer">
    <h1 class="block brand-title">Brightline Grins</h1>
    <p class="block tagline">Anyone can have a Hollywood Smile!</p>
    <div class="photo photo-portrait" role="img" aria-label="Soft portrait photograph with a bright white smile"></div>

    <div class="block info-panel">
      <p>we use a non peroxide gel so no sensitivity at all and completely pain free cosmetic procedure.</p>
      <p>we offer two different treatments…</p>
      <p>20 minute express £30 each or 2 people for £50</p>
      <p>45 minute premium (longer lasting) £50 each or 2 people for £80</p>
    </div>

    <div class="photo photo-teeth-before" role="img" aria-label="Close-up photograph of teeth before whitening"></div>
    <div class="photo photo-teeth-after" role="img" aria-label="Close-up photograph of teeth after whitening">
      <span class="after-label">AFTER</span>
    </div>
    <div class="photo photo-lips" role="img" aria-label="Close-up photograph of a smile half whitened"></div>

    <p class="block gift-note">I also do gift certificates perfect for birthdays christmas or just the one you love</p>

    <div class="block voucher voucher-smile">
      <p>Claim<br><span class="accent">a free top up pen</span><br>or<br>have an<br><span class="accent">extra 10%</span><br>off</p>
    </div>

    <address class="block contact-card contact-smile">
      <span>Rebecca Dowd</span>
      <span>01632960418</span>
      <span>27 Heol y Felin Pentwyn CF145QT</span>
      <span class="contact-email">dowdkevindowd@mailbox-example.co.uk</span>
    </address>
  </section>

</body>
</html>
```